Business card and stationery for an eCommerce store
Vornel Home Solutions
Business card and stationery for an eCommerce store - Retailers
Creative Brief
Simple
Tarin Velo K.M
Managing Partner
Vornel Home Solutions #254 , 6th B Cross, G D Layout, Hosadiga Ext, Kelnavadi, Bangalore - 560481
pkelmandro@vomta.in
www.vomta.in
Vornel Home Solutions is the private limited firm that owns vomta.in. Vornel Home Solutions doesn't have any separate identity/ logo created. In addition to business card design, I would also like to see designs for Letterhead and Envelope.
Concepts
Business Cards/Letterhead/ Envelopes/Notepads/Tshirt/labels for copper kite crate

```html
<!DOCTYPE html>
<html lang="en">
<head>
<meta charset="utf-8">
<title>Vornel Home Solutions – Stationery</title>
<link href="https://fonts.googleapis.com/css2?family=Open+Sans:wght@400;600;700&display=swap" rel="stylesheet">
<style>
  :root {
    --backdrop: #2e2e2e;
    --paper: #ffffff;
    --brand-red: #c7373a;
    --brand-orange: #f39a2b;
    --brand-wordmark: #d9462c;
    --ink: #555555;
    --ink-soft: #8a8a8a;
  }
  * { margin: 0; padding: 0; box-sizing: border-box; }
  html, body { width: 1200px; height: 647px; overflow: hidden; }
  body {
    background: var(--backdrop);
    font-family: "Open Sans", Arial, sans-serif;
    position: relative;
    color: var(--ink);
  }
  .sheet { position: absolute; background: var(--paper); box-shadow: 0 3px 10px rgba(0,0,0,.45); overflow: hidden; }

  .wordmark { display: flex; align-items: center; gap: 5px; font-weight: 700; color: var(--brand-wordmark); line-height: 1; }
  .wordmark .dot { border-radius: 50%; background: var(--brand-orange); flex: none; }

  .swoosh { position: absolute; left: 0; right: 0; height: 2px;
    background: linear-gradient(90deg, rgba(243,154,43,0) 0%, var(--brand-orange) 35%, var(--brand-red) 100%); }

  .small-text { font-size: 4px; line-height: 1.45; color: var(--ink-soft); }
  .small-text strong { color: var(--brand-wordmark); font-weight: 600; }

  /* Business card front */
  .card-front { left: 53px; top: 209px; width: 170px; height: 100px; border-radius: 4px; }
  .card-front .wordmark { position: absolute; left: 10px; top: 14px; font-size: 16px; }
  .card-front .wordmark .dot { width: 6px; height: 6px; }
  .card-front .company { position: absolute; left: 10px; top: 42px; }
  .card-front .person { position: absolute; left: 88px; top: 42px; }
  .card-front .person .name { font-size: 5px; font-weight: 700; color: var(--brand-wordmark); }
  .card-front .swoosh { bottom: 14px; }
  .card-front .web { position: absolute; right: 10px; bottom: 5px; font-size: 4px; color: var(--ink-soft); }

  /* Business card back */
  .card-back { left: 53px; top: 293px; width: 170px; height: 91px; border-radius: 4px; background: var(--brand-red); }
  .card-back .wordmark { position: absolute; left: 50%; top: 32px; transform: translateX(-50%); font-size: 18px; color: var(--paper); }
  .card-back .wordmark .dot { width: 7px; height: 7px; background: var(--paper); }
  .card-back .web { position: absolute; left: 0; right: 0; top: 60px; text-align: center; font-size: 4px; color: #f3c9c9; letter-spacing: .5px; }

  /* Letterhead */
  .letterhead { left: 247px; top: 24px; width: 406px; height: 595px; }
  .letterhead .wordmark { position: absolute; left: 30px; top: 56px; font-size: 24px; }
  .letterhead .wordmark .dot { width: 8px; height: 8px; }
  .letterhead .head-swoosh { position: absolute; left: 30px; top: 86px; width: 120px; height: 2px;
    background: linear-gradient(90deg, var(--brand-orange), rgba(243,154,43,0)); }
  .letterhead .contact { position: absolute; left: 262px; top: 52px; width: 120px; }
  .letterhead .swoosh { bottom: 24px; }
  .letterhead .web { position: absolute; left: 0; right: 0; bottom: 10px; text-align: center; font-size: 5px; letter-spacing: 1px; color: var(--ink-soft); }

  /* Envelope backs */
  .envelope-backs { left: 679px; top: 24px; width: 473px; height: 312px; background: transparent; box-shadow: none; }

  /* DL envelope front */
  .envelope-front { left: 679px; top: 384px; width: 473px; height: 204px; }
  .envelope-front .wordmark { position: absolute; left: 26px; top: 36px; font-size: 20px; }
  .envelope-front .wordmark .dot { width: 7px; height: 7px; }
  .envelope-front .return { position: absolute; left: 26px; top: 70px; }
  .envelope-front .swoosh { bottom: 22px; }
  .envelope-front .web { position: absolute; left: 0; right: 0; bottom: 8px; text-align: center; font-size: 5px; letter-spacing: 1px; color: var(--ink-soft); }
</style>
</head>
<body>

  <section class="sheet card-front" aria-label="Business card front">
    <div class="wordmark"><span class="dot"></span>vomta.in</div>
    <div class="company small-text">
      <strong>Vornel Home Solutions</strong><br>
      #254 , 6th B Cross, G D Layout,<br>
      Hosadiga Ext, Kelnavadi,<br>
      Bangalore - 560481
    </div>
    <div class="person small-text">
      <div class="name">Tarin Velo K.M</div>
      Managing Partner<br>
      Ph: 080 4100 2233<br>
      pkelmandro@vomta.in
    </div>
    <div class="swoosh"></div>
    <div class="web">www.vomta.in</div>
  </section>

  <section class="sheet card-back" aria-label="Business card back">
    <div class="wordmark"><span class="dot"></span>vomta.in</div>
    <div class="web">www.vomta.in</div>
  </section>

  <section class="sheet letterhead" aria-label="Letterhead">
    <div class="wordmark"><span class="dot"></span>vomta.in</div>
    <div class="head-swoosh"></div>
    <div class="contact small-text">
      <strong>Vornel Home Solutions</strong><br>
      Ph: 080 4100 2233<br>
      Mob: 98450 11223<br>
      pkelmandro@vomta.in<br>
      #254 , 6th B Cross, G D Layout,<br>
      Hosadiga Ext, Kelnavadi,<br>
      Bangalore - 560481
    </div>
    <div class="swoosh"></div>
    <div class="web">www.vomta.in</div>
  </section>

  <section class="sheet envelope-backs" aria-label="Envelope backs in white, red and orange">
    <svg width="473" height="312" viewBox="0 0 473 312">
      <rect x="0" y="0" width="473" height="312" fill="#ffffff"/>
      <polyline points="0,10 236,72 473,10" fill="none" stroke="#dddddd" stroke-width="1"/>
      <polygon points="0,60 473,60 473,110 236,170 0,110" fill="#c7373a"/>
      <polygon points="0,160 473,160 473,210 236,275 0,210" fill="#f39a2b"/>
      <line x1="0" y1="160" x2="473" y2="160" stroke="#ffffff" stroke-width="1"/>
    </svg>
  </section>

  <section class="sheet envelope-front" aria-label="Envelope front">
    <div class="wordmark"><span class="dot"></span>vomta.in</div>
    <div class="return small-text">
      <strong>Vornel Home Solutions</strong><br>
      #254 , 6th B Cross, G D Layout,<br>
      Hosadiga Ext, Kelnavadi,<br>
      Bangalore - 560481
    </div>
    <div class="swoosh"></div>
    <div class="web">www.vomta.in</div>
  </section>

</body>
</html>
```